Flyer
Zielgruppe
Ich bin eine professionelle Nail-Masterin . Meine Spezialität sind Gellacknägel. Hochprofessionelle Nägel für den Alltag bis hin zu speziellen Anlässen wie Hochzeit. Meine Arbeit steht für hochstehende Qualität die man sehen und fühlen kann. Die Zielgruppe sind Frauen die auf ihr äusseres achten und sich für spezielle Anlässe zurecht machen wollen.
Auf dem Flyer möchte ich den Start an meinem neuen Standort (Studen BE) promoten. Um meinen Kundenstamm aufzubauen werden Neukunden ein Angebot erhalten: Gellacknägel als Willkommensangebot für 49.- (SFr). Dieses Angebot ist pro Kunde nur einmalig gültig.
Terminvereinbarung per per SMS/Whatsapp 079/482 13 57 oder auf www.brivalack.ch
Aufgabenstellung
Völlig freie Hand beim Designen. Der Flyer wird per Post verteilt. Keine Falzflyer.

```html
<!DOCTYPE html>
<html lang="de">
<head>
<meta charset="utf-8">
<title>Brivalack Nails – Flyer</title>
<link href="https://fonts.googleapis.com/css2?family=Noto+Serif:wght@500;700&display=swap" rel="stylesheet">
<style>
  :root{
    --canvas:#e2e1df;
    --ink-dark:#120810;
    --plum:#3a1430;
    --berry:#8a2a62;
    --rose:#b94f86;
    --rose-light:#c45d92;
    --brush:#e2508f;
    --ring:#f6e4f1;
    --white:#ffffff;
  }
  *{margin:0;padding:0;box-sizing:border-box}
  html,body{width:1200px;height:1200px;overflow:hidden;background:var(--canvas)}
  body{position:relative;font-family:"Noto Serif",Georgia,serif;color:var(--white)}
  .flyer-side{position:absolute;left:299px;width:595px;overflow:hidden}
  .flyer-front{top:0;height:588px;
    background:
      radial-gradient(ellipse 60% 45% at 20% 70%, rgba(226,80,143,.45), transparent 70%),
      linear-gradient(180deg,var(--ink-dark) 0%,var(--plum) 30%,var(--berry) 65%,var(--rose) 100%);}
  .flyer-back{top:614px;height:586px;
    background:
      radial-gradient(ellipse 50% 30% at 70% 10%, rgba(170,50,150,.35), transparent 70%),
      linear-gradient(180deg,var(--ink-dark) 0%,#1c0a18 25%,var(--plum) 55%,var(--berry) 75%);}
  .art{position:absolute;left:0;top:0}
  .brand-name{position:absolute;left:45px;top:52px;font-weight:700;font-size:46px;line-height:1;letter-spacing:1px;color:var(--white)}
  .brand-name span{display:block;font-size:30px;letter-spacing:6px;margin-top:8px}
  .tagline{position:absolute;left:45px;top:197px;font-size:17px;font-weight:500;white-space:nowrap}
  .intro{position:absolute;left:45px;top:250px;font-size:17px;line-height:26.2px;font-weight:500;white-space:nowrap}
  .offer{position:absolute;left:35px;top:56px}
  .offer-line{display:block;background:var(--brush);font-size:20.5px;font-weight:500;line-height:30px;padding:0 5px;margin-bottom:2px;white-space:nowrap;border-radius:2px 6px 4px 3px}
  .contact-band{position:absolute;left:0;top:443px;width:595px;height:143px;background:linear-gradient(180deg,var(--rose) 0%,var(--rose-light) 100%)}
  .contact-title{position:absolute;left:37px;top:455px;font-size:18px;font-weight:500;white-space:nowrap}
  .contact-line{position:absolute;left:49px;font-size:20px;font-weight:500;white-space:nowrap}
  .contact-phone{top:496px}
  .contact-web{top:530px}
  .contact-web strong{margin-left:12px;font-weight:500;font-size:21px;letter-spacing:.5px}
</style>
</head>
<body>

<section class="flyer-side flyer-front">
  <svg class="art" width="595" height="588" viewBox="0 0 595 588">
    <defs>
      <linearGradient id="g-nails-lilac" x1="0" y1="0" x2="1" y2="1">
        <stop offset="0" stop-color="#c79f92"/><stop offset=".6" stop-color="#b5a0c4"/><stop offset="1" stop-color="#7f7b84"/>
      </linearGradient>
      <linearGradient id="g-nails-nude" x1="0" y1="0" x2="1" y2="1">
        <stop offset="0" stop-color="#d9a89a"/><stop offset=".5" stop-color="#e8cfcc"/><stop offset="1" stop-color="#6e6770"/>
      </linearGradient>
      <linearGradient id="g-nails-floral" x1="0" y1="0" x2="1" y2="1">
        <stop offset="0" stop-color="#e5c7c4"/><stop offset="1" stop-color="#cfc6bc"/>
      </linearGradient>
      <radialGradient id="g-polish" cx=".5" cy=".5" r=".5">
        <stop offset="0" stop-color="#e0298a"/><stop offset="1" stop-color="#e0298a" stop-opacity="0"/>
      </radialGradient>
    </defs>
    <ellipse role="img" aria-label="Umgekippte pinke Nagellackflasche mit Lackpfütze" cx="140" cy="500" rx="160" ry="70" fill="url(#g-polish)" opacity=".7"/>
    <g transform="rotate(9 420 230)">
      <rect x="322" y="30" width="215" height="440" rx="30" fill="#3a3a3c"/>
      <rect role="img" aria-label="Foto: Hand mit violett glitzernden Gellacknägeln" x="330" y="38" width="199" height="424" rx="24" fill="url(#g-nails-lilac)"/>
      <rect x="385" y="38" width="90" height="14" rx="7" fill="#111"/>
    </g>
    <circle cx="466" cy="435" r="109" fill="var(--ring)"/>
    <circle role="img" aria-label="Foto: Hand mit nudefarbenen und schwarzen Gellacknägeln" cx="466" cy="435" r="104" fill="url(#g-nails-nude)"/>
    <circle cx="323" cy="463" r="86" fill="var(--ring)"/>
    <circle role="img" aria-label="Foto: Hände mit zartrosa Nägeln und Blattdesign" cx="323" cy="463" r="81" fill="url(#g-nails-floral)"/>
  </svg>
  <div class="brand-name">BRIVALACK<span>NAILS</span></div>
  <p class="tagline">Qualität auf den ersten Blick</p>
  <p class="intro">Ich biete Ihnen hohe Qualität<br>und exaktes verarbeiten.<br>Qualität die Sie sehen<br>werden. Ob klassisch oder<br>ausgefallen, für den Alltag<br>bis hin zu<br>Hochzeitsdesign, bei<br>mir sind Ihre Nägel<br>in guten Händen</p>
</section>

<section class="flyer-side flyer-back">
  <svg class="art" width="595" height="586" viewBox="0 0 595 586">
    <defs>
      <linearGradient id="g-nails-peach" x1="0" y1="0" x2="1" y2="1">
        <stop offset="0" stop-color="#e9e6e0"/><stop offset=".45" stop-color="#d9a090"/><stop offset="1" stop-color="#ecd27a"/>
      </linearGradient>
      <linearGradient id="g-nails-grey" x1="0" y1="0" x2="1" y2="1">
        <stop offset="0" stop-color="#c99588"/><stop offset=".6" stop-color="#d8d2dc"/><stop offset="1" stop-color="#c6b3d8"/>
      </linearGradient>
      <radialGradient id="g-polish-back" cx=".5" cy=".5" r=".5">
        <stop offset="0" stop-color="#d81f7f"/><stop offset="1" stop-color="#d81f7f" stop-opacity="0"/>
      </radialGradient>
    </defs>
    <ellipse role="img" aria-label="Umgekippte pinke Nagellackflasche mit Lackpfütze" cx="470" cy="520" rx="150" ry="80" fill="url(#g-polish-back)" opacity=".8"/>
    <circle cx="375" cy="284" r="134" fill="var(--ring)"/>
    <circle role="img" aria-label="Foto: Hand mit pfirsichfarbenen Gellacknägeln auf gelbem Tuch" cx="375" cy="284" r="128" fill="url(#g-nails-peach)"/>
    <circle cx="201" cy="320" r="104" fill="var(--ring)"/>
    <circle role="img" aria-label="Foto: Hand mit hellgrauen Nägeln und Akzentnagel" cx="201" cy="320" r="98" fill="url(#g-nails-grey)"/>
  </svg>
  <div class="offer">
    <span class="offer-line">Gellacknägel als Willkommensangebot für 49</span>
    <span class="offer-line">Dieses Angebot ist pro Kunde nur einmalig gültig</span>
  </div>
  <div class="contact-band"></div>
  <p class="contact-title">Terminvereinbarung per per:</p>
  <p class="contact-line contact-phone">SMS/Whatsapp: 079/482 13 57</p>
  <p class="contact-line contact-web">oder auf:<strong>www.brivalack.ch</strong></p>
</section>

</body>
</html>
```